New Business Card Design Project

Need a design that will create an impact / strong impression towards our clients for our business. We are in the lighting business and we do lighting retrofits for large commercial to industrial clientele.

Target Market(s)

Lighting Industry

Industry/Entity Type

Business

Other font styles liked:
• we would like to use the font on our logo, not sure what it is though..

Requirements
Must have
• Our logo.
Nice to have
• We are open to suggestions that have to do with lighting.

```html
<!DOCTYPE html>
<html lang="en">
<head>
<meta charset="utf-8">
<title>Brightline Retrofit Group – Business Cards</title>
<link rel="stylesheet" href="https://fonts.googleapis.com/css2?family=Open+Sans:wght@400;600;700&display=swap">
<style>
  :root {
    --bg: #3a3a3a;
    --forest: #1d4526;
    --leaf: #6cc04a;
    --brand: #1f7a32;
    --ink-grey: #7a7a7a;
    --ink-dark: #3c3c3c;
    --paper: #ffffff;
  }
  * { margin: 0; padding: 0; box-sizing: border-box; }
  html, body {
    width: 1200px; height: 864px; overflow: hidden;
    background: var(--bg);
    font-family: "Open Sans", Arial, sans-serif;
  }
  .canvas { position: relative; width: 1200px; height: 864px; }
  .card {
    position: absolute; width: 560px; height: 320px;
    overflow: hidden; box-shadow: 0 10px 24px rgba(0,0,0,.45);
  }
  .card-front { left: 70px; top: 90px; background: var(--forest); }
  .card-back  { left: 570px; top: 450px; background: var(--paper); }

  .brand {
    position: absolute; display: flex; align-items: center; gap: 12px;
    font-weight: 700; font-size: 26px; letter-spacing: .5px; white-space: nowrap;
  }
  .brand-mark { width: 22px; height: 22px; }
  .card-front .brand { left: 50%; top: 50%; transform: translate(-50%, -50%); color: var(--paper); }
  .card-front .brand-mark { background: var(--paper); }
  .card-back .brand { left: 40px; top: 62px; font-size: 20px; color: var(--brand); }
  .card-back .brand-mark { width: 18px; height: 18px; background: var(--brand); }

  .band { position: absolute; inset: 0; width: 560px; height: 320px; }

  .person { position: absolute; left: 40px; top: 150px; }
  .person-name { font-size: 21px; font-weight: 600; color: var(--brand); line-height: 1.1; }
  .person-title { font-size: 15px; color: var(--ink-grey); margin-top: 2px; }

  .contacts { position: absolute; left: 40px; top: 212px; list-style: none; }
  .contacts li {
    display: flex; align-items: center; gap: 8px;
    font-size: 15px; color: var(--ink-dark); line-height: 21px;
  }
  .contacts svg { width: 12px; height: 12px; fill: var(--brand); flex: none; }

  .address {
    position: absolute; right: 18px; top: 236px;
    color: var(--paper); font-size: 14px; line-height: 21px;
    font-style: normal; text-align: left; white-space: nowrap;
  }
</style>
</head>
<body>
<main class="canvas">
  <section class="card card-front">
    <div class="brand"><span class="brand-mark"></span>Brightline Retrofit Group, LLC</div>
  </section>

  <section class="card card-back">
    <svg class="band" viewBox="0 0 560 320" aria-hidden="true">
      <polygon points="438,0 450,0 332,320 318,320" fill="var(--leaf)"/>
      <polygon points="458,0 560,0 560,320 340,320" fill="var(--forest)"/>
    </svg>

    <div class="brand"><span class="brand-mark"></span>Brightline Retrofit Group, LLC</div>

    <div class="person">
      <p class="person-name">John Smith</p>
      <p class="person-title">President</p>
    </div>

    <ul class="contacts">
      <li><svg viewBox="0 0 24 24"><path d="M6.6 10.8a15 15 0 0 0 6.6 6.6l2.2-2.2a1 1 0 0 1 1-.25 11.4 11.4 0 0 0 3.6.6 1 1 0 0 1 1 1V20a1 1 0 0 1-1 1A17 17 0 0 1 3 4a1 1 0 0 1 1-1h3.5a1 1 0 0 1 1 1c0 1.25.2 2.450.6 3.6a1 1 0 0 1-.25 1z"/></svg>01 012-345-6789</li>
      <li><svg viewBox="0 0 24 24"><path d="M7 1h10a2 2 0 0 1 2 2v18a2 2 0 0 1-2 2H7a2 2 0 0 1-2-2V3a2 2 0 0 1 2-2zm0 3v14h10V4z"/></svg>01 012-345-6780</li>
      <li><svg viewBox="0 0 24 24"><path d="M2 5h20v14H2zm2 2v.5l8 5 8-5V7z"/></svg>info@yourwebsite.com</li>
      <li><svg viewBox="0 0 24 24"><path d="M12 2a10 10 0 1 0 0 20 10 10 0 0 0 0-20zm6.9 9h-3a15 15 0 0 0-1.4-6A8 8 0 0 1 18.9 11zM12 4.1c.9 1.3 1.8 3.6 2 6.9h-4c.2-3.3 1.1-5.6 2-6.9zM9.5 5a15 15 0 0 0-1.4 6h-3A8 8 0 0 1 9.5 5zM5.1 13h3a15 15 0 0 0 1.4 6 8 8 0 0 1-4.4-6zm6.9 6.9c-.9-1.3-1.8-3.6-2-6.9h4c-.2 3.3-1.1 5.6-2 6.9zm2.5-.9a15 15 0 0 0 1.4-6h3a8 8 0 0 1-4.4 6z"/></svg>yourwebsite.com</li>
    </ul>

    <address class="address">
      Street Name, Suite 100<br>
      State, Zip Code, Country
    </address>
  </section>
</main>
</body>
</html>
```